Website Design

Need a professional, clean ( no clutter) and serious website designed for Commodities. As main element Energy: Oil & Gas, Coal, Biofuel and other tabs for other products such as agricultural products fresh fruits, Vegetable as well as grain: wheat, Soy Bean, rice, nuts and organic fertilizers and one whole organic section. Meat and poultry, Edible Oils, Real Estate Investments, Aviation products airplanes and engines.

New few nice pictures of refineries and anything that evokes a sense of Oil & Gas they're usually taken at night with lighting an illuminations will look good

I'm just throwing ideas and it will have to be clustered together with the appropriate category they belong: Canned products and I will get the rest later.

I'd like to make sure that the navigation in the website and the overall experience of people who visit this site is going to be superb.

I will check out your sample websites and see which ones will be a good start for the designers.

Down the road i want to be able to add sections that will require password to get in but that's probably a little bit later down the road.

Thank you all in advance and look forward to working with you. The Log you guys did magnificent. Please ask the support to let you have it. The color motives are dark blue, white and silver in the logo.
Thanks and regards,
Bilou

Target Market(s)

Commodity Traders ( not the stock market!) it's that actual tangible physical commodities.

Industry/Entity Type

It Professional

Number of Pages Required

5+ page

Requirements
Must have
• Need a professional, clean ( no clutter), elegant and serious website. Fonts to be a good match for our Logo fonts. I need the website to be scalable and can be added more pages as our need increases. this is for professionals to go this site and be able to navigate through the site without ever getting lost in it.

```html
<!DOCTYPE html>
<html lang="en">
<head>
<meta charset="utf-8">
<title>Meridian Crest Trading Group</title>
<link href="https://fonts.googleapis.com/css2?family=Open+Sans:wght@400;600;700;800&family=Oswald:wght@500;600&display=swap" rel="stylesheet">
<style>
:root{
  --navy:#0b2545;
  --navy-deep:#071a33;
  --blue:#1c5aa6;
  --blue-bright:#2a6fc4;
  --silver:#c9ced6;
  --grey-band:#e6e7e9;
  --grey-panel:#eeeeee;
  --grey-dark:#5a5d62;
  --card-cap:#3a3c40;
  --text:#444a52;
  --muted:#7b8087;
  --footer:#1d1f22;
  --footer-bottom:#141517;
  --white:#ffffff;
}
*{box-sizing:border-box;margin:0;padding:0}
html,body{width:1200px;height:2536px;overflow:hidden}
body{font-family:"Open Sans",Arial,sans-serif;color:var(--text);background:var(--white);font-size:13px;line-height:1.6}
.wrap{width:1000px;margin:0 auto;position:relative}

/* header */
.site-header{height:120px}
.site-header .wrap{height:120px;display:flex;align-items:center;justify-content:space-between}
.brand{display:flex;align-items:center;gap:12px}
.brand-mark{width:34px;height:34px;background:var(--navy)}
.brand-name{font-weight:800;color:var(--navy);font-size:22px;line-height:1.05;text-transform:uppercase;letter-spacing:.3px}
.header-side{display:flex;flex-direction:column;align-items:flex-end;gap:12px}
.contact-line{display:flex;gap:26px;font-size:11px;color:var(--muted)}
.contact-line span{display:flex;align-items:center;gap:6px}
.search{display:flex}
.search input{width:200px;height:28px;border:1px solid #d4d6d9;padding:0 10px;font:11px "Open Sans",sans-serif;color:var(--muted)}
.search button{height:28px;padding:0 12px;border:0;background:var(--grey-dark);color:#fff;font:11px "Open Sans",sans-serif}

/* nav */
.main-nav{height:56px;background:var(--navy)}
.main-nav ul{list-style:none;display:flex;height:56px;align-items:center;justify-content:space-between}
.main-nav li{font-size:11px;font-weight:600;color:var(--white);text-transform:uppercase;padding:0 6px;height:56px;display:flex;align-items:center}
.main-nav li.active{background:var(--blue-bright);padding:0 14px}

/* hero */
.hero{height:596px;position:relative;background:
  radial-gradient(ellipse at 55% 55%,rgba(255,176,74,.55),transparent 38%),
  radial-gradient(ellipse at 30% 60%,rgba(255,150,60,.35),transparent 30%),
  linear-gradient(180deg,#1f4f86 0%,#2e5f95 35%,#1a2f4d 62%,#0c1728 100%)}
.hero-arrow{position:absolute;top:270px;width:36px;height:56px;display:flex;align-items:center;justify-content:center}
.hero-arrow.prev{left:20px}.hero-arrow.next{right:20px}
.hero-caption{position:absolute;left:0;right:0;bottom:0;height:150px;background:rgba(5,14,28,.55);text-align:center;padding-top:28px;color:var(--white)}
.hero-caption h1{font-family:"Oswald","Open Sans",sans-serif;font-weight:600;font-size:36px;letter-spacing:1px;text-transform:uppercase}
.hero-caption p{font-size:14px;width:620px;margin:6px auto 0;line-height:1.5;color:#e2e6ec}

/* welcome */
.welcome{padding:72px 0 0;height:548px}
.welcome .wrap{display:flex;justify-content:space-between}
.welcome-main{width:640px}
.section-title{font-family:"Oswald","Open Sans",sans-serif;font-weight:500;font-size:28px;color:var(--navy);text-transform:uppercase;letter-spacing:.5px}
.welcome-main p{margin-top:16px;font-size:14px;width:470px}
.features{display:flex;gap:60px;margin-top:44px}
.feature{width:160px;text-align:center}
.feature-icon{width:84px;height:84px;border-radius:50%;border:2px solid var(--silver);margin:0 auto;display:flex;align-items:center;justify-content:center}
.feature h3{font-size:14px;font-weight:700;color:var(--navy);text-transform:uppercase;margin-top:14px}
.btn{display:inline-block;background:var(--navy);color:var(--white);font-size:11px;font-weight:700;text-transform:uppercase;padding:7px 14px;margin-top:12px}
.services{width:300px;margin-top:0}
.services h2{background:var(--grey-dark);color:var(--white);font-size:15px;font-weight:600;text-transform:uppercase;padding:16px 22px}
.services ul{list-style:none;background:var(--grey-panel);padding:20px 22px 26px}
.services li{font-size:14px;text-transform:uppercase;color:var(--text);line-height:30px;display:flex;align-items:center;gap:8px}
.services li::before{content:"";border-left:6px solid var(--navy);border-top:4px solid transparent;border-bottom:4px solid transparent}

/* what we do */
.what-we-do{background:var(--grey-band);height:410px;padding-top:36px}
.wwd-head{display:flex;align-items:center;justify-content:center;gap:20px}
.wwd-head::before,.wwd-head::after{content:"";height:1px;width:300px;background:#b9bcc1}
.wwd-head h2{font-family:"Oswald","Open Sans",sans-serif;font-weight:500;font-size:28px;color:var(--navy);text-transform:uppercase}
.carousel-ctrl{position:absolute;right:0;top:4px;display:flex;gap:4px}
.carousel-ctrl span{width:26px;height:22px;background:#9a9ea4;display:flex;align-items:center;justify-content:center}
.cards{display:flex;justify-content:space-between;margin-top:36px}
.card{width:318px}
.card-img{height:196px}
.card-img.oil{background:radial-gradient(ellipse at 45% 70%,#f5a94a,transparent 45%),linear-gradient(180deg,#22457a,#0f1f3a)}
.card-img.coal{background:linear-gradient(180deg,#8fa2b3 0%,#b7b2a5 45%,#5f5648 100%)}
.card-img.bio{background:radial-gradient(circle at 55% 40%,#fff4c8,transparent 30%),linear-gradient(180deg,#7fa2c8,#c9b079 70%,#3a3524)}
.card-cap{background:var(--card-cap);color:#d7d9dc;padding:16px 20px;height:96px}
.card-cap h3{font-size:14px;font-weight:700;color:var(--white);text-transform:uppercase}
.card-cap p{font-size:11px;line-height:1.5;margin-top:4px}

/* about */
.about{height:400px;padding-top:44px}
.about .wrap{display:flex;justify-content:space-between}
.about-text{width:520px}
.about-text h2{font-size:14px;font-weight:700;color:var(--blue);text-transform:uppercase}
.about-text p{font-size:12px;margin-top:12px;color:var(--muted)}
.about-img{width:440px;height:300px;background:radial-gradient(ellipse at 70% 35%,#f2a24c,transparent 30%),linear-gradient(180deg,#6f8cb0 0%,#3d5e87 45%,#1a2e4a 100%)}

/* footer */
.site-footer{background:var(--footer);height:360px;padding-top:34px;color:#a9adb3}
.site-footer .wrap{display:flex;justify-content:space-between}
.footer-col h4{font-size:13px;font-weight:700;color:var(--white);text-transform:uppercase;margin-bottom:14px}
.footer-links{width:240px}
.footer-links ul{list-style:none}
.footer-links li{font-size:11px;line-height:19px}
.socials{display:flex;gap:8px;margin-top:22px}
.socials span{width:34px;height:34px;border-radius:50%;background:#55585d}
.footer-news{width:300px}
.news-item{margin-bottom:14px}
.news-item p{font-size:11px;line-height:1.45}
.news-item time{font-size:10px;color:var(--blue-bright)}
.footer-news{margin-left:-80px}
.footer-newsletter{width:250px}
.footer-newsletter p{font-size:11px;margin-bottom:10px}
.footer-newsletter input{display:block;width:100%;height:30px;margin-bottom:10px;border:0;background:#f3f3f3;padding:0 10px;font:11px "Open Sans",sans-serif;color:var(--muted)}
.footer-newsletter button{border:0;background:var(--blue);color:#fff;font:700 11px "Open Sans",sans-serif;text-transform:uppercase;padding:8px 18px}
.footer-bottom{height:46px;background:var(--footer-bottom);font-size:10px;color:#7b7f85}
.footer-bottom .wrap{height:46px;display:flex;align-items:center;justify-content:space-between}
</style>
</head>
<body>

<header class="site-header">
  <div class="wrap">
    <div class="brand">
      <span class="brand-mark"></span>
      <span class="brand-name">Meridian Crest<br>Trading Group</span>
    </div>
    <div class="header-side">
      <div class="contact-line">
        <span><svg width="9" height="12" viewBox="0 0 9 12"><path d="M4.5 0a4.5 4.5 0 0 0-4.5 4.5C0 8 4.5 12 4.5 12S9 8 9 4.5A4.5 4.5 0 0 0 4.5 0zm0 6.3a1.8 1.8 0 1 1 0-3.6 1.8 1.8 0 0 1 0 3.6z" fill="#7b8087"/></svg>48 Harbour Row, Dunmore, DN4 7QE</span>
        <span><svg width="11" height="11" viewBox="0 0 24 24"><path d="M6.6 10.8a15 15 0 0 0 6.6 6.6l2.2-2.2a1 1 0 0 1 1-.25 11.4 11.4 0 0 0 3.6.57 1 1 0 0 1 1 1V20a1 1 0 0 1-1 1A17 17 0 0 1 3 4a1 1 0 0 1 1-1h3.5a1 1 0 0 1 1 1c0 1.25.2 2.45.57 3.57a1 1 0 0 1-.25 1z" fill="#7b8087"/></svg>+1 (555) 014 2280 | Support</span>
      </div>
      <form class="search"><input type="text" value="Search"><button type="button">Search</button></form>
    </div>
  </div>
</header>

<nav class="main-nav">
  <div class="wrap">
    <ul>
      <li class="active">Home</li><li>Oil &amp; Gas</li><li>Coal</li><li>Biofuel</li><li>Vegetable &amp; Fruits</li><li>Meat &amp; Poultry</li><li>Edible Oils</li><li>Real Estate Investments</li><li>Aviation Products</li><li>Contact Us</li>
    </ul>
  </div>
</nav>

<section class="hero" role="img" aria-label="Offshore oil platform lit up at night over the sea">
  <span class="hero-arrow prev"><svg width="16" height="30" viewBox="0 0 16 30"><path d="M14 2 2 15l12 13" stroke="rgba(255,255,255,.5)" stroke-width="3" fill="none"/></svg></span>
  <span class="hero-arrow next"><svg width="16" height="30" viewBox="0 0 16 30"><path d="M2 2l12 13L2 28" stroke="rgba(255,255,255,.5)" stroke-width="3" fill="none"/></svg></span>
  <div class="hero-caption">
    <h1>Pellentesque dapibus augue libero finibus</h1>
    <p>Aenean mi arcu, ultricies non euismod sit amet, suscipit eu tellus. Nulla facilisi. Ut et urna ac lectus feugiat fringilla ac sit amet dolor. Sed euismod semper</p>
  </div>
</section>

<section class="welcome">
  <div class="wrap">
    <div class="welcome-main">
      <h2 class="section-title">Welcome to Meridian Crest</h2>
      <p>Neque porro quisquam est qui dolorem ipsum quia dolor sit amet, consectetur, adipisci velit. There is no one who loves pain.</p>
      <div class="features">
        <div class="feature">
          <div class="feature-icon"><svg width="40" height="40" viewBox="0 0 40 40" fill="none" stroke="#1c5aa6" stroke-width="2.5"><circle cx="20" cy="13" r="6"/><path d="M8 34c0-7 5-11 12-11s12 4 12 11"/></svg></div>
          <h3>Project Management</h3>
          <span class="btn">Read More</span>
        </div>
        <div class="feature">
          <div class="feature-icon"><svg width="40" height="40" viewBox="0 0 40 40" fill="none" stroke="#1c5aa6" stroke-width="2.5"><circle cx="20" cy="20" r="14"/><ellipse cx="20" cy="20" rx="6" ry="14"/><path d="M6 20h28"/></svg></div>
          <h3>Global Safety</h3>
          <span class="btn">Read More</span>
        </div>
        <div class="feature">
          <div class="feature-icon"><svg width="40" height="40" viewBox="0 0 40 40" fill="none" stroke="#1c5aa6" stroke-width="2.5"><rect x="6" y="8" width="28" height="19" rx="1"/><path d="M15 33h10M20 27v6"/></svg></div>
          <h3>Computing Facilitie</h3>
          <span class="btn">Read More</span>
        </div>
      </div>
    </div>
    <aside class="services">
      <h2>Our Services</h2>
      <ul><li>Process</li><li>Instrument</li><li>Mechanical</li><li>Electrical</li><li>Structural</li><li>Pipeline</li><li>Management</li><li>Computing</li></ul>
    </aside>
  </div>
</section>

<section class="what-we-do">
  <div class="wrap">
    <div class="wwd-head"><h2>What we do</h2></div>
    <div class="carousel-ctrl">
      <span><svg width="8" height="10" viewBox="0 0 8 10"><path d="M6 1 2 5l4 4" stroke="#fff" stroke-width="2" fill="none"/></svg></span>
      <span><svg width="8" height="10" viewBox="0 0 8 10"><path d="M2 1l4 4-4 4" stroke="#fff" stroke-width="2" fill="none"/></svg></span>
    </div>
    <div class="cards">
      <article class="card">
        <div class="card-img oil" role="img" aria-label="Refinery towers glowing with lights at night"></div>
        <div class="card-cap"><h3>Oil &amp; Gas</h3><p>Aenean pulvinar elit eget dictum congue. Ut nec varius sem euismod convallis.</p></div>
      </article>
      <article class="card">
        <div class="card-img coal" role="img" aria-label="Large mining haul truck at a coal pit"></div>
        <div class="card-cap"><h3>Coal</h3><p>Aenean pulvinar elit eget dictum congue. Ut nec varius sem euismod convallis.</p></div>
      </article>
      <article class="card">
        <div class="card-img bio" role="img" aria-label="Oil pump jack against a bright sunset sky"></div>
        <div class="card-cap"><h3>Biofuel</h3><p>Aenean pulvinar elit eget dictum congue. Ut nec varius sem euismod convallis.</p></div>
      </article>
    </div>
  </div>
</section>

<section class="about">
  <div class="wrap">
    <div class="about-text">
      <h2>Nam condimentum massa sed vitae laoreet velit</h2>
      <p>Lorem Ipsum is simply dummy text of the printing and typesetting industry. Lorem Ipsum has been the industry's standard text ever since the early days.</p>
      <p>Standard dummy text ever since the 1500s, when an unknown printer took a galley of type and scrambled it to make a type specimen book. It has survived not only five centuries, but also the leap into electronic typesetting, remaining essentially unchanged. It was popularised in the 1960s with the release of sheets containing passages, and more recently with desktop publishing software like these layouts.</p>
      <span class="btn">Read More</span>
    </div>
    <div class="about-img" role="img" aria-label="Engineer in a hard hat overlooking an illuminated refinery at dusk"></div>
  </div>
</section>

<footer class="site-footer">
  <div class="wrap">
    <div class="footer-col footer-links">
      <h4>Meridian Crest</h4>
      <ul><li>Home</li><li>Oil &amp; Gas</li><li>Coal</li><li>Biofuel</li><li>Vegetable &amp; Fruits</li><li>Meat &amp; Poultry</li><li>Edible Oils</li><li>Real Estate Investments</li><li>Aviation Products</li></ul>
      <div class="socials"><span></span><span></span><span></span><span></span></div>
    </div>
    <div class="footer-col footer-news">
      <h4>Featured News &amp; Events</h4>
      <div class="news-item"><p>New trade routes opened for bulk grain shipments across the southern ports this season.</p><time>August 14, 2015</time></div>
      <div class="news-item"><p>Quarterly review of refined fuel supply and storage capacity now available to partners.</p><time>August 09, 2015</time></div>
      <div class="news-item"><p>Annual commodity forum announced, with sessions on energy, metals and agriculture.</p><time>August 02, 2015</time></div>
    </div>
    <div class="footer-col footer-newsletter">
      <h4>Newsletter Sign Up</h4>
      <p>Receive market updates in your inbox.</p>
      <input type="text" value="Name">
      <input type="text" value="Email">
      <input type="text" value="Company">
      <button type="button">Subscribe</button>
    </div>
  </div>
</footer>
<div class="footer-bottom">
  <div class="wrap"><span>© Copyright 2015 Meridian Crest Trading Group. All rights reserved.</span><span>↑ Top</span></div>
</div>

</body>
</html>
```